Präsentationsvorlagen für Unternehmensberatung im Finanzbereich
Zielgruppe
Unternehmensberatung für den Finanzbereich, Compliance Beratung/Implementierung regulatorischer Projekte, Bereitstellung von Management Resourcen, Trainings/Coaching/Seminare. Zielgruppe: Banken, Fonds und Investmentgesellschaften
Aufgabenstellung
hochwertiges design, clean, keine standard bilder von Bergen, Tastaturen oder Menschen, die sich unterhalten. eher Architektur Bilder, Bilder sollen Bezug zum Inhalt haben, Verlässlichkeit, Professionalität, Kundenfokus ausstrahlen. 4 Services sollen präsentiert werden, ggf mit Bildlogo in unterschiedlichen Farben verbinden.

```html
<!DOCTYPE html>
<html lang="en">
<head>
<meta charset="utf-8">
<title>Brevard Sàrl – Presentation Templates</title>
<link href="https://fonts.googleapis.com/css2?family=Montserrat:wght@400;500;600&display=swap" rel="stylesheet">
<style>
  :root {
    --ink: #353a45;
    --paper: #ffffff;
    --mist: #ececec;
    --stone: #d9d5cf;
    --shadow: rgba(0,0,0,.28);
  }
  html, body { margin: 0; padding: 0; overflow: hidden; }
  body {
    width: 1200px; height: 849px; position: relative;
    background: var(--paper);
    font-family: "Montserrat", sans-serif; color: var(--ink);
  }
  .slide {
    position: absolute; width: 322px; height: 181px; overflow: hidden;
    box-shadow: 4px 4px 5px var(--shadow);
    background: var(--paper);
  }
  .slide--dark { background: var(--ink); color: var(--paper); }
  .slide svg.art { position: absolute; inset: 0; width: 100%; height: 100%; }
  .brand-name {
    position: absolute; font-weight: 500; letter-spacing: .18em;
    text-transform: uppercase; color: var(--ink); white-space: nowrap;
  }
  .slide--dark .brand-name { color: var(--paper); }
  .section-title {
    position: absolute; left: 19px; top: 19px; margin: 0;
    font-weight: 400; font-size: 11.5px; line-height: 12px; letter-spacing: .02em;
    text-transform: uppercase;
  }

  /* Title slide */
  .title-slide { left: 215px; top: 85px; }
  .title-slide .brand-name { left: 170px; top: 92px; font-size: 13px; }
  .title-slide .brand-sub { position: absolute; left: 170px; top: 110px; width: 114px; text-align: center; font-size: 7px; letter-spacing: .3em; }
  .title-slide .subtitle { position: absolute; left: 150px; top: 145px; font-size: 14.5px; }

  /* Executive summary */
  .summary-slide { left: 649px; top: 85px; }
  .summary-slide h2 { position: absolute; left: 18px; top: 18px; margin: 0; font-size: 12px; font-weight: 600; }
  .summary-slide .brand-name { right: 16px; top: 40px; font-size: 6px; }
  .summary-list { position: absolute; left: 20px; top: 49px; margin: 0; padding: 0; list-style: none; }
  .summary-list li { display: flex; align-items: center; height: 23px; margin-bottom: 7.5px; font-size: 9.5px; font-weight: 500; }
  .summary-list .num {
    width: 23px; height: 23px; border-radius: 50%; background: var(--paper); color: var(--ink);
    display: flex; align-items: center; justify-content: center; font-size: 9px; font-weight: 600; margin-right: 12px;
  }

  /* About */
  .about-slide { left: 43px; top: 327px; }
  .about-slide h2 { position: absolute; left: 75px; top: 47px; margin: 0; font-size: 12px; font-weight: 600; }
  .about-slide .brand-name { right: 11px; top: 36px; font-size: 6px; }
  .about-list { position: absolute; left: 75px; top: 72px; width: 180px; margin: 0; padding: 0 0 0 8px; font-size: 8.6px; line-height: 12.2px; }

  .directorships-slide { left: 432px; top: 327px; }
  .directorships-slide .brand-name { right: 16px; top: 21px; font-size: 7px; }
  .coaching-slide-a { left: 821px; top: 327px; }
  .coaching-slide-b { left: 215px; top: 568px; }
  .coaching-slide-a .brand-name, .coaching-slide-b .brand-name { right: 12px; top: 21px; font-size: 7px; }
  .aml-slide { left: 649px; top: 568px; }
  .aml-slide .brand-name { right: 10px; top: 120px; font-size: 7px; }
</style>
</head>
<body>

<section class="slide title-slide">
  <svg class="art" viewBox="0 0 322 181" role="img" aria-label="Photo of palm leaf shadows on a stone wall">
    <defs><linearGradient id="stone" x1="0" y1="0" x2="1" y2="1">
      <stop offset="0" stop-color="#e6e2dc"/><stop offset=".5" stop-color="#c9c5bf"/><stop offset="1" stop-color="#dedad4"/></linearGradient></defs>
    <path d="M0 0 L128 0 C142 35 142 100 118 135 C98 162 76 178 62 181 L0 181 Z" fill="url(#stone)"/>
  </svg>
  <div class="brand-name">Brevard</div>
  <div class="brand-sub">SÀRL</div>
  <div class="subtitle">Untertitel, 18.04.2023</div>
</section>

<section class="slide slide--dark summary-slide">
  <svg class="art" viewBox="0 0 322 181" role="img" aria-label="Photo of light and palm shadows on a white wall">
    <defs><linearGradient id="wall" x1="0" y1="0" x2="1" y2="0">
      <stop offset="0" stop-color="#e4e4e4"/><stop offset=".5" stop-color="#f4f4f4"/><stop offset="1" stop-color="#dcdcdc"/></linearGradient></defs>
    <path d="M322 68 C262 68 184 80 170 122 C162 148 170 168 186 181 L322 181 Z" fill="url(#wall)"/>
  </svg>
  <h2>EXECUTIVE SUMMARY</h2>
  <div class="brand-name">Brevard</div>
  <ul class="summary-list">
    <li><span class="num">01</span>Lorem Impsum</li>
    <li><span class="num">02</span>Lorem Impsum</li>
    <li><span class="num">03</span>Lorem Impsum</li>
    <li><span class="num">04</span>Lorem Impsum</li>
  </ul>
</section>

<section class="slide about-slide">
  <svg class="art" viewBox="0 0 322 181" role="img" aria-label="Photo of white diagonal architectural ribs">
    <defs><linearGradient id="ribs" x1="0" y1="0" x2="1" y2="1">
      <stop offset="0" stop-color="#efefef"/><stop offset=".5" stop-color="#fbfbfb"/><stop offset="1" stop-color="#e9e9e9"/></linearGradient></defs>
    <rect width="322" height="181" fill="url(#ribs)"/>
  </svg>
  <div class="brand-name">Brevard</div>
  <h2>ABOUT</h2>
  <ul class="about-list">
    <li>18+ years of experience in the financial sector</li>
    <li>Qualified lawyer</li>
    <li>10+ years in Executive and Board positions</li>
    <li>4 jurisdictions</li>
  </ul>
</section>

<section class="slide directorships-slide">
  <svg class="art" viewBox="0 0 322 181" role="img" aria-label="Photo of soft diagonal light on a pale wall">
    <defs><linearGradient id="light" x1="0" y1="0" x2="1" y2="1">
      <stop offset="0" stop-color="#dcdcdc"/><stop offset=".45" stop-color="#f6f6f6"/><stop offset=".7" stop-color="#e2e2e2"/><stop offset="1" stop-color="#f2f2f2"/></linearGradient></defs>
    <rect width="322" height="181" fill="url(#light)"/>
  </svg>
  <h2 class="section-title">Independent Directorships/<br>RC Mandates</h2>
  <div class="brand-name">Brevard</div>
</section>

<section class="slide slide--dark coaching-slide-a">
  <svg class="art" viewBox="0 0 322 181" role="img" aria-label="Photo of a curling white paper page">
    <defs><linearGradient id="curl" x1="0" y1="0" x2="1" y2="1">
      <stop offset="0" stop-color="#f6f6f6"/><stop offset=".4" stop-color="#d8dadc"/><stop offset="1" stop-color="#f3f3f3"/></linearGradient></defs>
    <path d="M212 0 C190 40 175 82 175 122 C175 150 178 166 185 181 L322 181 L322 0 Z" fill="url(#curl)"/>
  </svg>
  <h2 class="section-title">Couching/Trainings</h2>
  <div class="brand-name">Brevard</div>
</section>

<section class="slide slide--dark coaching-slide-b">
  <svg class="art" viewBox="0 0 322 181" role="img" aria-label="Photo of a curling white paper page">
    <path d="M212 0 C190 40 175 82 175 122 C175 150 178 166 185 181 L322 181 L322 0 Z" fill="url(#curl)"/>
  </svg>
  <h2 class="section-title">Couching/Trainings</h2>
  <div class="brand-name">Brevard</div>
</section>

<section class="slide aml-slide">
  <svg class="art" viewBox="0 0 322 181" role="img" aria-label="Photo of a white room with columns and a green monstera plant">
    <defs>
      <linearGradient id="room" x1="0" y1="0" x2="1" y2="0">
        <stop offset="0" stop-color="#dedede"/><stop offset=".3" stop-color="#f2f2f2"/><stop offset=".6" stop-color="#e6e6e6"/><stop offset="1" stop-color="#ededed"/></linearGradient>
      <radialGradient id="plant" cx=".8" cy=".25" r=".3">
        <stop offset="0" stop-color="#7fae6a"/><stop offset="1" stop-color="#7fae6a" stop-opacity="0"/></radialGradient>
    </defs>
    <rect width="322" height="181" fill="url(#room)"/>
    <rect y="150" width="322" height="31" fill="#d8d8d8"/>
    <rect width="322" height="181" fill="url(#plant)"/>
  </svg>
  <h2 class="section-title">AML/CTF Support</h2>
  <div class="brand-name">Brevard</div>
</section>

</body>
</html>
```